Stationery Required - Own Logo provided

Hi,

We are a retail company called 'Copperfinch Trading Limited' based in the UK and would like some corporate stationery designed.

We have provided our Logo which we would like to use (Its attached to this brief)...

The designs must be orginal, professional, stylish and interesting!

Target Market(s)

We will use this stationery to communicate with our wholesale suppliers and employees, so it must have a 'professional' feel about it.

Industry/Entity Type

It Company

Requirements
Must have
• Must be professional, corporate, stylish and not to 'fussy'. we require ... Business card design, a4 letter, compliment slip. All designs must be supplied in a format where the text (address/telephone numbers etc..) can be edited, as we have alot of staff and operate out of several different premises.
Nice to have
• I would like a windows backround picture file supplied as well so we can integrate that onto our computer systems.

```html
<!DOCTYPE html>
<html lang="en">
<head>
<meta charset="utf-8">
<title>Copperfinch Trading Limited – Business Card</title>
<link rel="stylesheet" href="https://fonts.googleapis.com/css2?family=Open+Sans:wght@400&display=swap">
<style>
  :root {
    --leaf-dark: #3b5e10;
    --leaf-bright: #80ff00;
    --ink: #111111;
    --paper: #ffffff;
  }
  html, body {
    margin: 0;
    padding: 0;
    width: 1200px;
    height: 780px;
    overflow: hidden;
    background: var(--paper);
  }
  .card {
    position: relative;
    width: 1200px;
    height: 780px;
    background: var(--paper);
    font-family: "Open Sans", Arial, sans-serif;
    overflow: hidden;
  }
  .brand {
    position: absolute;
    left: 120px;
    top: 150px;
    display: flex;
    align-items: center;
    gap: 30px;
  }
  .brand-mark {
    width: 96px;
    height: 96px;
    background: var(--leaf-bright);
    flex: none;
  }
  .brand-name {
    margin: 0;
    font-size: 50px;
    font-weight: 400;
    color: var(--leaf-dark);
    white-space: nowrap;
    letter-spacing: 0.5px;
  }
  .brand-rule {
    position: absolute;
    left: 0;
    top: 302px;
    width: 1000px;
    height: 4px;
    background: var(--leaf-dark);
  }
  .holder {
    position: absolute;
    left: 620px;
    transform: translateX(-50%);
    text-align: center;
    margin: 0;
    white-space: nowrap;
    color: var(--ink);
    font-weight: 400;
  }
  .holder-name {
    top: 390px;
    font-size: 37px;
  }
  .holder-title {
    top: 446px;
    font-size: 26px;
  }
  .contact {
    position: absolute;
    left: 620px;
    top: 536px;
    transform: translateX(-50%);
    margin: 0;
    text-align: center;
    font-style: normal;
    white-space: nowrap;
    color: var(--leaf-dark);
    font-size: 28px;
    line-height: 41px;
    letter-spacing: 0.3px;
  }
  .contact span { display: block; }
  .footer-band {
    position: absolute;
    left: 0;
    top: 690px;
    width: 1200px;
    height: 90px;
    background: var(--leaf-bright);
  }
</style>
</head>
<body>
  <main class="card">
    <header class="brand">
      <div class="brand-mark" aria-hidden="true"></div>
      <h1 class="brand-name">Copperfinch Trading Limited</h1>
    </header>
    <div class="brand-rule" aria-hidden="true"></div>

    <p class="holder holder-name">ROWAN ELLERY</p>
    <p class="holder holder-title">COMPANY DIRECTOR</p>

    <address class="contact">
      <span>P. 07700900418</span>
      <span>E. copperfinch@example.com</span>
      <span>17 mill lane, Ballyholt, County Down BT99 4QR</span>
    </address>

    <div class="footer-band" aria-hidden="true"></div>
  </main>
</body>
</html>
```